Creative & Professional Business Card for hair salon

We are looking to update our business cards. Our salon is creative, modern, progressive and professional and looking for a design that will reflect this.

```html
<!DOCTYPE html>
<html lang="en">
<head>
<meta charset="utf-8">
<title>Silver Lining Studio – Business Card</title>
<link rel="stylesheet" href="https://fonts.googleapis.com/css2?family=Arimo:wght@400;700&family=Lato:wght@300&display=swap">
<style>
  :root {
    --backdrop: #2a2a2a;
    --card: #f3f3f2;
    --accent: #6b9ab0;
    --accent-dark: #4d89a6;
    --ink: #3c3c3c;
    --ink-soft: #555555;
    --white: #ffffff;
  }
  * { box-sizing: border-box; margin: 0; padding: 0; }
  html, body { width: 1200px; height: 960px; overflow: hidden; }
  body {
    position: relative;
    background: var(--backdrop);
    font-family: "Arimo", Arial, sans-serif;
  }
  .card {
    position: absolute;
    width: 600px;
    height: 342px;
    background: var(--card);
    border-radius: 22px;
    overflow: hidden;
  }
  .card--front { left: 314px; top: 113px; }
  .card--back  { left: 311px; top: 472px; }

  .cloud-panel {
    position: absolute;
    left: 200px;
    top: -40px;
    width: 420px;
    height: 314px;
    background: var(--accent);
    border-radius: 0 0 0 170px;
  }
  .holder {
    position: absolute;
    right: 36px;
    top: 70px;
    text-align: right;
    color: var(--white);
  }
  .holder__name { font-weight: 700; font-size: 25px; line-height: 30px; }
  .holder__role { font-size: 16px; line-height: 18px; }

  .contacts {
    position: absolute;
    left: 40px;
    top: 232px;
    list-style: none;
    font-size: 14px;
    color: var(--ink);
  }
  .contacts li {
    display: flex;
    align-items: center;
    height: 19px;
  }
  .contacts svg { width: 13px; height: 13px; margin-right: 8px; fill: var(--accent); }
  .address {
    position: absolute;
    right: 36px;
    top: 290px;
    font-size: 14px;
    color: var(--ink);
  }

  .brand {
    position: absolute;
    left: 0;
    right: 0;
    top: 178px;
    text-align: center;
    font-family: "Lato", Arial, sans-serif;
    font-weight: 300;
    font-size: 30px;
    color: var(--accent-dark);
  }
  .web {
    position: absolute;
    left: 0;
    right: 0;
    top: 294px;
    text-align: center;
    font-size: 14px;
    letter-spacing: 3px;
    color: var(--ink-soft);
  }
</style>
</head>
<body>
  <section class="card card--front">
    <div class="cloud-panel" role="img" aria-label="Swirling cloud decoration in soft blue"></div>
    <div class="holder">
      <p class="holder__name">Mark Ellison</p>
      <p class="holder__role">CEO/Founder</p>
    </div>
    <ul class="contacts">
      <li><svg viewBox="0 0 16 16" aria-hidden="true"><path d="M3.6 1.2l2.3 2.6-1.3 1.9c.9 2 2.4 3.6 4.6 4.8l1.8-1.3 2.8 2.2-1.4 2.6C7.4 13.8 2.3 8.7 1.2 3.1z"/></svg>07 5120 4398</li>
      <li><svg viewBox="0 0 16 16" aria-hidden="true"><path d="M1 3h14v10H1z M2 4l6 5 6-5" stroke="#f3f3f2" stroke-width="1.2"/></svg>salon@silverliningstudio.com.ac</li>
      <li><svg viewBox="0 0 16 16" aria-hidden="true"><circle cx="8" cy="8" r="7"/><path d="M1 8h14M8 1c-3 3-3 11 0 14M8 1c3 3 3 11 0 14" stroke="#f3f3f2" stroke-width="1" fill="none"/></svg>www.silverliningstudio.com.ac</li>
      <li><svg viewBox="0 0 16 16" aria-hidden="true"><circle cx="8" cy="8" r="7"/></svg>SilverLiningbyLenaMoretti</li>
    </ul>
    <p class="address">5/27 Ocean Lane, Kelwin</p>
  </section>

  <section class="card card--back">
    <p class="brand">Silver Lining Studio</p>
    <p class="web">www.silverliningstudio.com.ac</p>
  </section>
</body>
</html>
```